TEALDOCK Lunch and Learn Presentation

We are hosting a live lunch and learn and need to create a presentation for our company. Here is an outline of what is needed and I want to have someone use our new brand logo, colors, and fonts to create an engaging presentation.
Here is the outline.
3. Copy, Layout & Directions for Each Slide
Slide 1: Title
Background: Blue gradient (top left to bottom right) or a subtle tech pattern
Header:
TEALDOCK Lunch & Learn
Subtext:
Smarter business communication starts here
Details (bottom):
September 1, 2025 | Vorna Offices
Logo Placeholder: Centered above or below the title (add after your logo file is available)
Design Tip: Keep plenty of whitespace. Use white or light grey for text.
Slide 2: Who We Are
Layout: Split screen.
Left: “Formerly TeDOCK” with old logo placeholder
Right: “Now TEALDOCK” with new logo placeholder
Below: Timeline or row of company milestones
Key Points (bullets):
Local expertise with national reach
Over [X] years helping businesses stay connected
Rebranded from TeDOCK → TEALDOCK for clarity, growth, and innovation
Visual: Leave space for graphics or timeline (add later)
Slide 3: Why the Rebrand?
Background: Subtle grey tech pattern or white
Big Visual:
Word cloud or three large, bold text words across the slide:
Clarity | Innovation | Future-Ready
Bullets:
To eliminate confusion in the market
To reflect our expanded solutions & AI innovation
To position our partners and customers for the future
Slide 4: Our Mission
Background: White with blue accent bar at top/bottom
Mission Statement (big/bold):
“Helping businesses never miss a call and improving how people connect.”
Key Points (bullets):
Reliable communications made simple
Technology + human-first service
Tools that free up people to do what they do best
Placeholder: For a photo (collaborating team, handshake, etc.)
Slide 5: Platform Overview
Header:
TEALDOCK Relay
Icons: Row/circle with: Phone | Text bubble | Globe/portal | Support team
Features (bullets):
Business-class phone system
Core calling features + voicemail
Business texting & mobility
Easy-to-manage web portal
Backed by our support team
Design Tip: Use blue for icons, grey for text
Slide 6: Key Differentiators
Layout: 2-column comparison table
Left: TEALDOCK (Blue background, white text, checkmarks)
Right: National Carriers (Grey or white background, minimal checkmarks)
Bullets:
Local support, national scalability
Flexible solutions (not one-size-fits-all)
AI-powered features (Brightwire)
Transparent pricing & partner-first approach
Slide 7: Demo Flow
Header:
How Relay Works in Action
Diagram:
Icons in horizontal order:
[Phone] → [AI/robot] → [Staff] → [Dashboard]
Steps:
Customer calls/texts in
Brightwire AI Receptionist answers (if enabled)
FAQs / scheduling handled automatically
Human team picks up higher-value conversations
Everything tracked in one platform
Slide 8: Spotlight: Brightwire AI Receptionist
Layout: Side-by-side (two columns)
Left: “Without Brightwire” (small icons for missed calls, stressed staff)
Right: “With Brightwire” (happy customers, productive staff)
Key Features (bullets):
Answers calls 24/7
Handles FAQs instantly
Schedules appointments
Frees staff to focus on relationships
Key Message:
Brightwire = your first line of support, not a replacement for people
Slide 9: Customer Story / Use Case
Header:
Example: HVAC Service Company
Layout: Split screen
Left: “Before” (chaotic image/placeholder), bullets:
Missed after-hours calls
Overwhelmed front desk
Right: “After” (organized image/placeholder), bullets:
Brightwire handled 60% of inbound calls
No missed opportunities
Staff had time for complex customer needs
Slide 10: Partner & Customer Benefits
Header:
Key Benefits
Checklist with icons (row or column):
Never miss a call or opportunity
Improve customer satisfaction & retention
Boost staff productivity
Gain a competitive edge with AI-powered communications
Dedicated local support team
Design Tip: Use blue/grey icons, white background
Slide 11: What’s Next?
Header:
What’s Next?
Bullets (with icons):
Try Brightwire AI Receptionist free trial
Explore Relay for smarter calling
Partner with TEALDOCK for growth opportunities
CTA Visual:
Bold blue rectangle/banner with white CTA text (Try Now, Explore, Partner)
Slide 12: Thank You / Q&A
Header:
Questions?
Subtext:
Let’s talk about how TEALDOCK can help your business never miss a call.
Footer:
TEALDOCK Logo (placeholder)
Contact: info@gettealdock.com
Website: www.gettealdock.com
Background: Blue or white, with blue text

```html
<!DOCTYPE html>
<html lang="en">
<head>
<meta charset="utf-8">
<title>Lunch and Learn – Our Mission</title>
<link rel="stylesheet" href="https://fonts.googleapis.com/css2?family=Montserrat:wght@500;700&display=swap">
<style>
  :root {
    --stage: #4d4d4d;
    --slide: #ffffff;
    --brand-blue: #0a96ee;
    --text-grey: #666a70;
    --photo-light: #dfe8f6;
    --photo-mid: #8fa9dc;
    --photo-deep: #1f3f86;
  }
  * { margin: 0; padding: 0; box-sizing: border-box; }
  html, body {
    width: 1200px; height: 801px; overflow: hidden;
    background: var(--stage);
    font-family: "Montserrat", Arial, sans-serif;
  }
  .slide {
    position: absolute; left: 58px; top: 96px;
    width: 1084px; height: 608px;
    background: var(--slide); overflow: hidden;
  }
  .photo {
    position: absolute; left: 494px; top: 0;
    width: 590px; height: 420px;
    background:
      radial-gradient(ellipse at 72% 45%, rgba(31,63,134,0.55), rgba(143,169,220,0.35) 45%, rgba(255,255,255,0) 75%),
      linear-gradient(90deg, rgba(255,255,255,1) 0%, var(--photo-light) 25%, var(--photo-mid) 60%, var(--photo-deep) 100%);
    -webkit-mask-image: linear-gradient(180deg, #000 65%, transparent 100%);
            mask-image: linear-gradient(180deg, #000 65%, transparent 100%);
  }
  .accent-lines { position: absolute; inset: 0; pointer-events: none; }
  .content { position: absolute; left: 91px; top: 0; }
  .title {
    position: absolute; top: 153px; left: 0; white-space: nowrap;
    font-weight: 700; font-size: 53.5px; line-height: 1;
    color: var(--brand-blue);
  }
  .statement {
    position: absolute; top: 220px; left: 0; width: 440px;
    font-weight: 500; font-size: 18.2px; line-height: 22px;
    color: var(--text-grey);
  }
  .points { position: absolute; top: 344px; left: 0; list-style: none; }
  .points li {
    white-space: nowrap; height: 58px;
    font-weight: 500; font-size: 18.2px; line-height: 22px;
    color: var(--text-grey);
  }
  .points li::after {
    content: ""; display: block; margin-top: 4px;
    width: 73px; height: 6px; background: var(--brand-blue);
  }
</style>
</head>
<body>
  <section class="slide">
    <div class="photo" role="img" aria-label="Photo of a business handshake in blue tones with a faint world map overlay"></div>

    <svg class="accent-lines" width="1084" height="608" viewBox="0 0 1084 608" fill="none" stroke="#0a96ee" stroke-width="1.2">
      <path d="M806 0 L912 58 L912 300 Q912 348 870 366 L380 608"/>
      <path d="M908 0 L923 8 L923 276 Q923 322 884 336 L323 608"/>
      <path d="M1084 312 L630 536 Q592 556 588 608"/>
      <path d="M1084 342 L614 572 Q598 582 575 608"/>
    </svg>

    <div class="content">
      <h1 class="title">Our Mission</h1>
      <p class="statement">Helping businesses never miss a call and improving how people connect.</p>
      <ul class="points">
        <li>Reliable communications made simple</li>
        <li>Technology + human-first service</li>
        <li>Tools that free people to do what they do best</li>
      </ul>
    </div>
  </section>
</body>
</html>
```